Redesign - Trifold Brochure - Adding new and fresh look.

I have attached what we currently have as a brochure but we need it to be redesigned. The information content is accurate but looking for fresh new design/layout. Please see the images attached. In tif and pdf format. If you need a different format to work please specify and will do my best to upload it.

Target Market(s)

Retail giveaways to educate customers.

Requirements
Must have
• New fresh look

```html
<!DOCTYPE html>
<html lang="en">
<head>
<meta charset="utf-8">
<title>Meadowline Botanicals – Trifold Brochure</title>
<link rel="stylesheet" href="https://fonts.googleapis.com/css2?family=Montserrat:wght@400;500;600;700&display=swap">
<style>
  :root {
    --orange: #f28c1e;
    --orange-deep: #e9791a;
    --green: #8dc63f;
    --grey-bar: #8e8e8e;
    --ink: #333333;
    --ink-soft: #4a4a4a;
    --paper: #ffffff;
    --backdrop: #e9e7e4;
    --diagram-dark: #0d2a33;
  }
  * { box-sizing: border-box; margin: 0; padding: 0; }
  html, body { width: 1200px; height: 1200px; overflow: hidden; }
  body {
    background: var(--backdrop);
    font-family: "Montserrat", sans-serif;
    color: var(--ink);
    position: relative;
  }
  .spread {
    position: absolute;
    left: 264px;
    width: 672px;
    height: 520px;
    background: var(--paper);
    box-shadow: 0 6px 18px rgba(0,0,0,.25);
    overflow: hidden;
  }
  .spread--outside { top: 48px; }
  .spread--inside { top: 632px; }
  .panel { position: absolute; top: 0; height: 100%; }
  .fold-shade::after {
    content: ""; position: absolute; top: 0; right: 0; width: 14px; height: 100%;
    background: linear-gradient(to right, rgba(0,0,0,0), rgba(0,0,0,.07));
  }
  .abs { position: absolute; }

  /* ---------- outside: FAQ panel ---------- */
  .faq { left: 0; width: 224px; }
  .faq__photo {
    left: 18px; top: 13px; width: 186px; height: 96px;
    background: linear-gradient(135deg, #d9d6cf 0%, #b9a36a 35%, #7a5a33 70%, #c9c4b9 100%);
  }
  .faq__caption {
    left: 18px; top: 109px; width: 186px; height: 32px;
    background: var(--green); color: #fff;
    font-size: 6.8px; line-height: 1.35; text-align: center; padding: 3px 4px;
  }
  .faq__title {
    left: 10px; top: 156px; width: 204px; text-align: center;
    font-size: 9.8px; font-weight: 500; line-height: 1.3;
  }
  .faq__bar {
    left: 18px; width: 186px; background: var(--grey-bar); color: #fff;
    font-size: 7.8px; font-weight: 600; text-align: center; line-height: 1.6;
    padding: 2px 4px;
  }
  .faq__text {
    left: 18px; width: 186px; font-size: 7.9px; line-height: 1.3;
    text-align: justify; color: var(--ink-soft);
  }

  /* ---------- outside: contact panel ---------- */
  .contact {
    left: 224px; width: 225px;
    background: linear-gradient(160deg, #f7a23b 0%, var(--orange) 55%, var(--orange-deep) 100%);
  }
  .contact__brand {
    left: 0; top: 296px; width: 100%; text-align: center;
    color: #fff; font-size: 9px; font-weight: 500;
  }
  .contact__brand .dot {
    display: block; width: 34px; height: 34px; border-radius: 50%;
    background: #fff; opacity: .9; margin: 0 auto 10px;
  }
  .contact__text {
    left: 17px; width: 200px; font-size: 7.8px; line-height: 1.32; color: #2b2b2b;
  }
  .contact__text strong { font-weight: 600; }

  /* ---------- outside: cover panel ---------- */
  .cover { left: 449px; width: 223px; }
  .cover__photo {
    left: 0; top: 0; width: 100%; height: 372px;
    background: linear-gradient(180deg, #9fd3ef 0%, #e6f4fb 28%, #ffffff 42%, #7fae5e 62%, #4f8a3a 78%, #ece3b4 90%, #ffffff 100%);
  }
  .cover__brand {
    left: 0; top: 34px; width: 100%; text-align: center;
    font-size: 9.5px; font-weight: 500; color: var(--ink-soft);
  }
  .cover__brand .dot {
    display: block; width: 36px; height: 36px; border-radius: 50%;
    background: var(--green); margin: 0 auto 8px;
  }
  .cover__tagline {
    left: 10px; top: 104px; width: 203px; text-align: center;
    font-size: 9.5px; font-weight: 700; line-height: 1.3; color: var(--ink);
  }
  .cover__question {
    left: 0; top: 386px; width: 100%; text-align: center;
    font-size: 10px; font-weight: 700;
  }
  .cover__titlebox {
    left: 14px; top: 405px; width: 195px; height: 73px;
    border: 1px solid #cfcfcf; text-align: center; padding-top: 5px;
    font-weight: 600; line-height: 1.05;
  }
  .cover__titlebox .t1 { color: var(--orange); font-size: 19px; letter-spacing: .5px; display: block; }
  .cover__titlebox .t2 { color: var(--green); font-size: 14.5px; display: block; margin: 2px 0; }
  .cover__titlebox .t3 { color: var(--orange); font-size: 19px; display: block; }
  .cover__sub {
    left: 0; top: 483px; width: 100%; text-align: center;
    font-size: 9.8px; font-weight: 700;
  }
  .cover__web {
    left: 0; bottom: 0; width: 100%; height: 18px; background: var(--orange);
    color: #fff; font-size: 7.6px; letter-spacing: 1.6px; text-align: center; line-height: 18px; font-weight: 500;
  }

  /* ---------- inside: intro panel ---------- */
  .intro { left: 0; width: 224px; }
  .intro__photo {
    left: 0; top: 0; width: 224px; height: 250px;
    background: linear-gradient(150deg, #7a3a10 0%, #d98a1c 30%, #f3c45a 50%, #b7472a 70%, #e9d8b8 100%);
  }
  .intro__heading {
    left: 17px; top: 258px; font-size: 10.5px; font-weight: 600; color: var(--orange);
  }
  .intro__text {
    left: 17px; top: 274px; width: 190px; font-size: 7.7px; line-height: 1.3;
    text-align: justify; color: var(--ink-soft);
  }
  .intro__lead {
    left: 17px; top: 370px; font-size: 7.8px; font-weight: 700;
  }
  .relief { left: 20px; top: 389px; width: 190px; }
  .relief__item {
    position: absolute; display: flex; align-items: center; gap: 8px;
    font-size: 7.8px; line-height: 1.25; color: var(--ink);
  }
  .relief__icon {
    flex: none; width: 20px; height: 20px; border-radius: 50%;
    background: var(--orange); border: 2px solid #f7c58c;
    display: flex; align-items: center; justify-content: center;
  }
  .intro__web {
    left: 0; top: 495px; width: 224px; text-align: center;
    font-size: 7.6px; letter-spacing: 1.5px; font-weight: 500;
  }

  /* ---------- inside: science panel ---------- */
  .science { left: 224px; width: 448px; }
  .science__title {
    left: 17px; top: 22px; width: 412px; height: 26px; background: var(--orange);
    color: #fff; font-size: 14.5px; font-weight: 600; text-align: center; line-height: 26px;
  }
  .science__text {
    left: 17px; top: 60px; width: 420px; font-size: 7.9px; line-height: 1.3;
    text-align: justify; color: var(--ink-soft);
  }
  .diagram {
    left: 17px; top: 153px; width: 412px; height: 279px;
    background: radial-gradient(circle at 20% 50%, #2a8fa6 0%, #123c48 35%, transparent 60%),
                radial-gradient(circle at 75% 55%, #d7461e 0%, #7a2a18 30%, transparent 55%),
                var(--diagram-dark);
  }
  .diagram__note {
    position: absolute; background: #fff; color: #333;
    font-size: 6.8px; line-height: 1.3; text-align: center; padding: 4px 4px;
  }
  .benefits {
    left: 17px; top: 436px; width: 412px; height: 66px; background: var(--green);
    color: #1e1e1e; font-size: 7.8px; line-height: 1.35; padding: 5px 7px;
  }
  .benefits__head { font-weight: 700; margin-bottom: 5px; }
  .benefits__cols { display: flex; }
  .benefits__col { display: flex; gap: 4px; font-weight: 500; }
  .benefits__col:first-child { width: 218px; }
</style>
</head>
<body>

<!-- ================= OUTSIDE ================= -->
<section class="spread spread--outside" aria-label="Brochure outside">

  <div class="panel faq fold-shade">
    <div class="abs faq__photo" role="img" aria-label="Photo of a glass bottle of hemp oil beside a bowl of hemp seeds"></div>
    <p class="abs faq__caption">Hemp derived products are widely thought to be the most nutritionally complete supplement source in the world.</p>
    <h2 class="abs faq__title">The Most Common Questions Associated with CBD Use:</h2>

    <div class="abs faq__bar" style="top:190px">Will I get “high” or feel “loaded”?</div>
    <p class="abs faq__text" style="top:222px">The answer is, “No.” Industrial hemp derived CBD will not make you feel euphoric. If you feel this way from a CBD product, it does not solely contain CBD &amp; may contain synthetics or other compounds not listed on the la-bel and should not be used.</p>

    <div class="abs faq__bar" style="top:291px">Is it legal?</div>
    <p class="abs faq__text" style="top:324px">Yes. Industrial hemp derived CBD con-tains very low to no THC levels which is the compound that makes Marijuana illegal. Industrial hemp products con-taining levels of THC ranging from 0% to 0.03% can be purchased from regu-lar retailers and are legal in all 50 states.</p>

    <div class="abs faq__bar" style="top:408px; height:34px; padding-top:3px">How can I take CBD?<br>How much CBD should I take?</div>
    <p class="abs faq__text" style="top:458px">CBD comes in many forms: Tinctures, edibles, vaporizable liquids, capsules, powders, as well as topical creams and salves.</p>
  </div>

  <div class="panel contact fold-shade">
    <div class="abs contact__brand"><span class="dot"></span>Meadowline Botanicals</div>
    <p class="abs contact__text" style="top:394px">If you would like to receive more information or purchase Meadowline Botanicals products,<br><strong>please contact:</strong><br>customerservice@MeadowlineBotanicals.com</p>
    <p class="abs contact__text" style="top:452px">If you would like to become a wholesale partner of Meadowline Botanicals,<br><strong>please send all wholesale inquiries to:</strong><br>wholesale@MeadowlineBotanicals.com</p>
  </div>

  <div class="panel cover">
    <div class="abs cover__photo" role="img" aria-label="Photo of young hemp plants under a bright sky with four bottles of the company's supplements in front"></div>
    <div class="abs cover__brand"><span class="dot"></span>Meadowline Botanicals</div>
    <p class="abs cover__tagline">Healthier Living Through Quality Products</p>
    <p class="abs cover__question">Can CBD Products Help Me?</p>
    <h1 class="abs cover__titlebox">
      <span class="t1">UNDERSTANDING</span>
      <span class="t2">Your Endocannabinoid</span>
      <span class="t3">SYSTEM</span>
    </h1>
    <p class="abs cover__sub">Putting the Pieces Together</p>
    <div class="abs cover__web">www.meadowlinebotanicals.com</div>
  </div>
</section>

<!-- ================= INSIDE ================= -->
<section class="spread spread--inside" aria-label="Brochure inside">

  <div class="panel intro fold-shade">
    <div class="abs intro__photo" role="img" aria-label="Close-up photo of golden oil dripping from a dropper into a small glass"></div>
    <h2 class="abs intro__heading">What is CBD?</h2>
    <p class="abs intro__text">CBD stands for Canna-bi-dy-all. CBD is one of many compounds called phytocan-nabi-noids that is found in various plant species. The industrial hemp plant is a plentiful source of CBD. When derived from industrial hemp, CBD with less than 0.03% THC by weight has no psychoactive properties but retains all of its positive bio-</p>
    <p class="abs intro__lead">CBD is commonly used as relief from:</p>
    <div class="abs relief">
      <div class="relief__item" style="left:0;top:0"><span class="relief__icon"><svg width="10" height="10" viewBox="0 0 10 10"><circle cx="5" cy="5" r="3" fill="none" stroke="#fff" stroke-width="1.2"/></svg></span>Pain</div>
      <div class="relief__item" style="left:100px;top:0"><span class="relief__icon"><svg width="10" height="10" viewBox="0 0 10 10"><rect x="1" y="4" width="8" height="3" fill="#fff"/><rect x="1" y="2" width="2" height="2" fill="#fff"/></svg></span>Sleep<br>Disorders</div>
      <div class="relief__item" style="left:0;top:32px"><span class="relief__icon"><svg width="10" height="10" viewBox="0 0 10 10"><circle cx="5" cy="3" r="2" fill="#fff"/><rect x="3" y="5" width="4" height="4" fill="#fff"/></svg></span>Inflammation</div>
      <div class="relief__item" style="left:100px;top:32px"><span class="relief__icon"><svg width="10" height="10" viewBox="0 0 10 10"><ellipse cx="5" cy="5" rx="4" ry="3" fill="none" stroke="#fff" stroke-width="1.2"/></svg></span>Neurological<br>Disorders</div>
      <div class="relief__item" style="left:0;top:64px"><span class="relief__icon"><svg width="10" height="10" viewBox="0 0 10 10"><circle cx="5" cy="5" r="4" fill="none" stroke="#fff" stroke-width="1.2"/><path d="M3 6 Q5 4 7 6" stroke="#fff" fill="none"/></svg></span>Anxiety</div>
      <div class="relief__item" style="left:100px;top:64px"><span class="relief__icon"><svg width="10" height="10" viewBox="0 0 10 10"><rect x="1" y="3.5" width="8" height="3" rx="1.5" fill="#fff" transform="rotate(-40 5 5)"/></svg></span>Opiate<br>Dependence</div>
    </div>
    <p class="abs intro__web">www.meadowlinebotanicals.com</p>
  </div>

  <div class="panel science">
    <h2 class="abs science__title">How Does CBD Work In Your Body?</h2>
    <p class="abs science__text">Your body produces certain natural compounds called cannabinoids that are used to regulate func-tions for your entire body. Inside your body there is a processing network for cannabinoids called your Endo-cannabinoid System. CBD mimics the natural cannabinoids produced by your body and stimulates certain receptors found on the surface of cells in your body that effect your ECS. These cells are mainly located in the central nervous system and the immune system. This reaction caused by the in-troduction of CBD helps balance and maintain and restore your body’s natural function. Es-sentially</p>

    <div class="abs diagram" role="img" aria-label="Illustration of a glowing human figure and a brain showing where cannabinoid receptors are found">
      <svg class="abs" style="left:0;top:0" width="412" height="279" viewBox="0 0 412 279" aria-hidden="true">
        <rect x="259" y="86" width="130" height="142" rx="12" fill="none" stroke="#f5a623" stroke-width="2"/>
        <path d="M115 78 L140 78 M115 160 L140 160 M115 240 L140 240 M230 240 L250 228" stroke="#e8e8e8" stroke-width=".8" fill="none"/>
      </svg>
      <div class="diagram__note" style="left:142px;top:42px;width:86px">CB2 receptors are predominantly found in the immune system.</div>
      <div class="diagram__note" style="left:142px;top:118px;width:86px">CB1 and CB2 receptors are found on the surface of cells in your body that effect your endo-canna-binoid system.</div>
      <div class="diagram__note" style="left:142px;top:216px;width:86px">CB2 receptors are responsible for the regulation of inflamma-tion which in turn reduces pain.</div>
      <div class="diagram__note" style="left:274px;top:216px;width:114px">CB1 receptors are found primarily in the brain controlling memory processing, motor regulation, appetite, pain sensation, mood, and sleep.</div>
    </div>

    <div class="abs benefits">
      <p class="benefits__head">There are many other benefits from using CBD and hemp products. Hemp products are:</p>
      <div class="benefits__cols">
        <div class="benefits__col"><span>High In :</span><span>Omega 3 and 6 Fatty Acids<br>Vitamins A &amp; E<br>Calcium, Iron &amp; Antioxidants</span></div>
        <div class="benefits__col"><span>Low In:</span><span>Saturated Fats<br>Cholesterol<br>Carbohydrates</span></div>
      </div>
    </div>
  </div>
</section>

</body>
</html>
```